Website page design

Hi, I need to improve the look of my homepage and the final offer page of my website. www.Pebble7dock.com We have an orvex buyback program where we purchase used orvex products from consumers nationwide. If you would go click through a sample offer on the site, you will the last view final offer page where we give you a cash offer for you site. I would like to keep the red and white colors since my logo is red and white. Please pay attention to the information shown on the homepage now, it is important for me to show the visitors this information on the home page. I would also love to give the users a friendly and inviting look when clicking on the options of orvex products on the home page.

Target Market(s)

Orvex electronics consumers

Number of Pages Required

2 page

Requirements
Nice to have
• On the final offer page, i would love for the offer to give an exciting look for the pebble 7 dock offer, and a boring look for the orvex buy back offer. At the final offer page you will my websites offer ( Your Pebble7dock Offer ) vs ( Orvex buyback program offer ) which is my competitor.

```html
<!DOCTYPE html>
<html lang="en">
<head>
<meta charset="utf-8">
<title>Pebble7dock – Sell Your Device</title>
<link href="https://fonts.googleapis.com/css2?family=Montserrat:wght@500;600;700;800&family=Nunito+Sans:wght@400;600;700&display=swap" rel="stylesheet">
<style>
:root{
  --red:#d0202a;
  --red-dark:#b3161f;
  --ink:#111111;
  --text:#3c3c3c;
  --muted:#6b6b6b;
  --line:#cfcfcf;
  --band:#f1f1f1;
  --sky:#cdebf1;
  --footer:#232427;
  --navy:#1b2340;
  --white:#ffffff;
}
*{box-sizing:border-box;margin:0;padding:0}
html,body{width:1200px;height:2617px;overflow:hidden}
body{position:relative;background:var(--white);font-family:"Nunito Sans",Arial,sans-serif;color:var(--text)}
.abs{position:absolute}

/* header */
.site-header{position:absolute;left:0;top:0;width:1200px;height:44px;background:var(--red)}
.brand{position:absolute;left:234px;top:11px;display:flex;align-items:center;gap:8px;color:var(--white);font-family:"Montserrat",sans-serif;font-weight:600;font-size:16px;letter-spacing:.5px}
.brand-dot{width:18px;height:18px;border-radius:50%;background:var(--white)}
.main-nav{position:absolute;top:15px;font-family:"Montserrat",sans-serif;font-size:10.5px;font-weight:500;color:var(--white)}
.auth-box{position:absolute;left:832px;top:0;width:133px;height:44px;background:var(--ink);clip-path:polygon(0 0,100% 0,100% 100%,0 100%,10px 50%);color:var(--white);font-family:"Montserrat",sans-serif;font-size:10.5px;font-weight:600;display:flex;align-items:center;justify-content:center;gap:9px;padding-left:10px}

/* hero */
.hero{position:absolute;left:0;top:44px;width:1200px;height:571px;background:linear-gradient(120deg,#ffffff 0%,#f7f7f7 45%,#ececec 100%);overflow:hidden}
.hero-title{position:absolute;left:239px;top:128px;font-family:"Montserrat",sans-serif;font-weight:700;font-size:26px;color:var(--ink);border-bottom:3px double #bbb;padding-bottom:1px}
.hero-copy{position:absolute;left:240px;top:186px;width:305px;font-size:10.4px;line-height:16.3px;color:var(--text)}
.hero-copy p+p{margin-top:16px}
.btn-red{position:absolute;background:var(--red);color:var(--white);border-radius:3px;font-family:"Montserrat",sans-serif;font-weight:600;display:flex;align-items:center;justify-content:center;box-shadow:0 4px 10px rgba(208,32,42,.3)}

/* badges */
.badge-band{position:absolute;left:0;top:615px;width:1200px;height:203px;background:var(--band)}
.badge{position:absolute;top:59px;height:88px;background:var(--white);box-shadow:0 2px 8px rgba(0,0,0,.08);display:flex;align-items:center;justify-content:center}
.badge-shape{width:60%;height:26px;border-radius:4px;background:#e2e2e2}

/* how it works */
.question-bar{position:absolute;left:302px;top:886px;width:595px;height:40px;background:var(--sky);clip-path:polygon(3px 0,100% 0,100% 100%,0 100%);display:flex;align-items:center;justify-content:center;gap:6px;font-size:14.5px;color:var(--ink)}
.question-bar .ico{width:20px;height:20px;border-radius:50%;background:var(--ink);color:var(--white);font-weight:700;font-size:13px;display:flex;align-items:center;justify-content:center}
.question-bar strong{font-family:"Montserrat",sans-serif;font-weight:600;font-size:14px}
.steps-banner{position:absolute;left:301px;top:1007px;width:230px;height:90px;background:var(--ink);clip-path:polygon(0 0,208px 0,100% 50%,208px 100%,0 100%);color:var(--white);padding:24px 0 0 22px;font-family:"Montserrat",sans-serif}
.steps-banner .small{font-size:13.5px;font-weight:500}
.steps-banner .big{font-size:24px;font-weight:800;margin-top:2px}
.step{position:absolute;top:995px;width:140px;text-align:center}
.step-icon{width:80px;height:80px;margin:0 auto;border:2px solid #e6e6e6;border-radius:50%;display:flex;align-items:center;justify-content:center;background:var(--white)}
.step-title{margin-top:16px;font-size:11.5px;font-weight:600;color:var(--ink)}
.step-sub{font-size:9.5px;line-height:11.5px;color:var(--text);margin-top:3px}

/* offer form */
.form-title{position:absolute;font-family:"Montserrat",sans-serif;font-weight:500;font-size:14.5px;color:var(--ink)}
.device{position:absolute;top:1207px;width:82px;height:72px;border:2px solid var(--line);border-radius:4px;display:flex;align-items:center;justify-content:center;background:var(--white)}
.device.is-active{border-color:var(--red)}
.device-label{position:absolute;top:1288px;width:82px;text-align:center;font-size:11px;color:var(--ink)}
.select{position:absolute;left:530px;width:366px;height:31px;border:2px solid #dcdcdc;border-radius:3px;font-size:10.5px;color:var(--ink);padding:7px 11px;background:var(--white)}
.select::after{content:"";position:absolute;right:13px;top:9px;width:6px;height:6px;border-right:1px solid #999;border-bottom:1px solid #999;transform:rotate(45deg)}
.offer-col{position:absolute;text-align:center}
.offer-label{font-family:"Montserrat",sans-serif;font-size:12px;font-weight:500;color:var(--ink);line-height:15px}
.offer-price{font-family:"Montserrat",sans-serif;font-weight:600;font-size:48px;color:var(--ink);line-height:52px}
.offer-note{font-size:12px;color:var(--muted);line-height:15px}
.vs{position:absolute;left:704px;top:1671px;width:32px;height:32px;border-radius:50%;background:#e5e5e5;font-size:12px;color:#444;display:flex;align-items:center;justify-content:center}

/* promo slider */
.promo{position:absolute;left:0;top:1906px;width:1200px;height:443px;background:radial-gradient(ellipse at 55% 70%,#ffffff 0%,#eaf6f9 40%,#cbe9f0 100%)}
.promo-title{position:absolute;left:188px;top:146px;width:300px;font-family:"Montserrat",sans-serif;color:var(--navy);font-size:36px;line-height:34px;letter-spacing:-1px;white-space:nowrap}
.promo-title .b{font-weight:800}
.promo-title .m{font-weight:500}
.promo-btn{position:absolute;left:190px;top:277px;width:133px;height:32px;background:var(--navy);border-radius:3px;color:var(--white);font-family:"Montserrat",sans-serif;font-weight:700;font-size:12px;display:flex;align-items:center;justify-content:center}
.slider-arrow{position:absolute;top:204px;width:56px;height:57px;background:var(--white);display:flex;align-items:center;justify-content:center}
.promo-devices{position:absolute;left:512px;top:135px;width:548px;height:228px;border-radius:6px;background:linear-gradient(100deg,#3c4a66 0%,#5a6684 45%,#c8364f 62%,#2b2b33 100%);opacity:.9}

/* footer */
.site-footer{position:absolute;left:0;top:2349px;width:1200px;height:268px;background:var(--footer);color:#cfcfcf}
.footer-brand{position:absolute;left:235px;top:60px;display:flex;align-items:center;gap:9px;font-family:"Montserrat",sans-serif;font-weight:600;font-size:20px;color:var(--white);letter-spacing:.5px}
.footer-brand .dot{width:24px;height:24px;border-radius:50%;background:var(--white)}
.footer-copy{position:absolute;left:236px;top:109px;width:393px;font-size:9.3px;line-height:15px}
.footer-copy p+p{margin-top:15px}
.contact{position:absolute;left:842px;top:80px;font-size:9.5px;line-height:15px}
.contact h3{font-family:"Montserrat",sans-serif;font-weight:600;font-size:14px;color:var(--white);margin-bottom:6px}
.contact strong{color:var(--white)}
.socials{display:flex;gap:6px;margin-top:8px}
.socials span{width:19px;height:19px;border:1px solid #cfcfcf;border-radius:50%}
.to-top{position:absolute;left:1115px;top:123px;width:36px;height:36px;border-radius:50%;background:#3b3c40;display:flex;align-items:center;justify-content:center}
</style>
</head>
<body>

<header class="site-header">
  <div class="brand"><span class="brand-dot"></span>PEBBLE7DOCK</div>
  <nav>
    <span class="main-nav" style="left:665px">HOME</span>
    <span class="main-nav" style="left:721px">TRACK</span>
    <span class="main-nav" style="left:780px">SELL</span>
  </nav>
  <div class="auth-box"><span>LOGIN</span><span style="font-weight:400">|</span><span>SIGNUP</span></div>
</header>

<section class="hero">
  <svg class="abs" style="left:0;top:0" width="1200" height="571" aria-hidden="true">
    <path d="M150 120 C 300 420, 560 560, 760 500 C 900 460, 1050 330, 1200 100 L1200 0 L1050 0 C 900 250, 700 380, 560 360 C 380 330, 260 220, 150 120 Z" fill="#ffffff" opacity=".7"/>
  </svg>
  <h1 class="hero-title">WHO WE ARE</h1>
  <div class="hero-copy">
    <p>Intellegi quidem, ut propter aliam quampiam rem, verbi gratia propter voluptatem, nos amemus; Quia nec honesto quic quam honestius nec turpi turpius. Eorum enim omnium multa praetermittentium, dum eligant aliquid, quod sequantur, quasi curta sententia; Quid de Pythagora? Hoc mihi cum tuo fratre convenit.</p>
    <p>Eorum enim omnium multa praetermittentium, dum eligant aliquid, quod sequantur, quasi curta sententia; Quid de Pythagora? Hoc mihi cum tuo fratre convenit.</p>
  </div>
  <a class="btn-red" style="left:240px;top:377px;width:164px;height:38px;font-size:14px">Discover More...</a>
  <div class="abs" style="left:712px;top:170px;width:190px;height:200px;border-radius:50%;background:radial-gradient(circle,#a3a3a3 0%,#8d8d8d 100%)"></div>
</section>

<section class="badge-band" aria-label="Partner listings">
  <div class="badge" style="left:153px;width:149px"><div class="badge-shape"></div></div>
  <div class="badge" style="left:317px;width:238px"><div class="badge-shape"></div></div>
  <div class="badge" style="left:570px;width:148px"><div class="badge-shape"></div></div>
  <div class="badge" style="left:733px;width:149px"><div class="badge-shape"></div></div>
  <div class="badge" style="left:897px;width:149px"><div class="badge-shape"></div></div>
</section>

<svg class="abs" style="left:0;top:818px" width="1200" height="1088" aria-hidden="true">
  <path d="M0 0 L230 260 Q250 290 230 320 L0 600 Z" fill="#f6f6f6"/>
  <path d="M1200 450 L1200 1088 L1170 1088 L1020 790 Z" fill="#f6f6f6"/>
</svg>

<div class="question-bar"><span class="ico">?</span>Have a question?&nbsp;<strong>Call us or send a text to 555-201-4478</strong></div>

<div class="steps-banner"><div class="small">CASH-IN YOUR DEVICE</div><div class="big">EASY AS 1-2-3</div></div>

<div class="step" style="left:523px">
  <div class="step-icon"><svg width="40" height="40" viewBox="0 0 40 40" fill="none" stroke="#111" stroke-width="2.5"><path d="M6 20 L20 6 L34 6 L34 20 L20 34 Z"/><circle cx="27" cy="13" r="2.5"/></svg></div>
  <div class="step-title">Get An Offer</div>
  <div class="step-sub">Less than a minute</div>
</div>
<div class="step" style="left:662px">
  <div class="step-icon"><svg width="46" height="34" viewBox="0 0 46 34" fill="none" stroke="#111" stroke-width="2.5"><rect x="2" y="4" width="26" height="20"/><path d="M28 10 H37 L44 17 V24 H28"/><circle cx="11" cy="27" r="4" fill="#fff"/><circle cx="36" cy="27" r="4" fill="#fff"/></svg></div>
  <div class="step-title">Ship it Free</div>
  <div class="step-sub">We provide a pre-paid<br>shipping label</div>
</div>
<div class="step" style="left:792px">
  <div class="step-icon"><svg width="42" height="30" viewBox="0 0 42 30" fill="none" stroke="#111" stroke-width="2.5"><rect x="2" y="2" width="38" height="26" rx="3"/><circle cx="21" cy="15" r="6"/></svg></div>
  <div class="step-title">Get Paid Fast</div>
  <div class="step-sub">Tallowpay, check or<br>bank transfer</div>
</div>

<div class="abs" role="img" aria-label="Illustration of a friendly bearded man in a green dollar-sign shirt pointing at the offer form" style="left:250px;top:1252px;width:250px;height:448px;border-radius:40px;background:linear-gradient(180deg,#e9d2bd 0%,#3f9c64 35%,#2f8a55 55%,#1c1c1c 75%,#3a3a3a 100%);opacity:.85"></div>

<div class="form-title" style="left:527px;top:1175px">Select Your Device</div>

<div class="device is-active" style="left:530px"><svg width="42" height="44" viewBox="0 0 42 44" fill="none" stroke="#bbb" stroke-width="1.5"><rect x="2" y="2" width="22" height="38" rx="3"/><rect x="26" y="14" width="14" height="28" rx="2"/></svg></div>
<div class="device" style="left:624px"><svg width="42" height="46" viewBox="0 0 42 46" fill="none" stroke="#bbb" stroke-width="1.5"><rect x="4" y="2" width="32" height="42" rx="3"/><rect x="9" y="7" width="22" height="32"/></svg></div>
<div class="device" style="left:719px"><svg width="50" height="44" viewBox="0 0 50 44" fill="none" stroke="#bbb" stroke-width="1.5"><rect x="2" y="2" width="46" height="30" rx="2"/><path d="M20 32 L18 40 H32 L30 32"/></svg></div>
<div class="device" style="left:815px"><svg width="56" height="36" viewBox="0 0 56 36" fill="none" stroke="#bbb" stroke-width="1.5"><rect x="8" y="3" width="40" height="26" rx="2"/><path d="M2 31 H54 L51 34 H5 Z"/></svg></div>
<div class="device-label" style="left:533px">Ophone</div>
<div class="device-label" style="left:624px">Otab</div>
<div class="device-label" style="left:719px">Odesk</div>
<div class="device-label" style="left:815px">Obook</div>

<div class="form-title" style="left:530px;top:1320px">Select Model</div>
<div class="select" style="top:1342px">Ophone X</div>
<div class="form-title" style="left:530px;top:1395px">Select a Carrier</div>
<div class="select" style="top:1416px">Northwire</div>
<div class="form-title" style="left:530px;top:1470px">Select Storage Size</div>
<div class="select" style="top:1491px">64 GB</div>
<div class="form-title" style="left:530px;top:1545px">Select a Condition</div>
<div class="select" style="top:1566px">Flawless</div>

<div class="offer-col" style="left:522px;top:1626px;width:160px">
  <div class="offer-label">Your<br>Pebble7dock Offer</div>
  <div class="offer-price">$840</div>
  <div class="offer-note">offer valid for 30 days</div>
</div>
<div class="vs">VS</div>
<div class="offer-col" style="left:756px;top:1634px;width:160px">
  <div class="offer-label">ABC Company</div>
  <div class="offer-price" style="margin-top:4px">$690</div>
  <div class="offer-note" style="margin-top:6px">Orvex buyback<br>program offer</div>
</div>
<a class="btn-red" style="left:534px;top:1764px;width:123px;height:38px;font-size:14.5px">Sell Now</a>

<section class="promo">
  <div class="promo-title"><div class="b">SELL</div><div class="m">YOUR DEVICE</div><div class="b">@ BEST PRICE</div></div>
  <a class="promo-btn">VIEW DETAILS</a>
  <div class="promo-devices" role="img" aria-label="Product photo of a laptop, tablet, phone and streaming box side by side"></div>
  <div class="slider-arrow" style="left:0"><svg width="14" height="22" viewBox="0 0 14 22" fill="none" stroke="#222" stroke-width="2"><path d="M11 2 L3 11 L11 20"/></svg></div>
  <div class="slider-arrow" style="left:1139px;width:61px"><svg width="14" height="22" viewBox="0 0 14 22" fill="none" stroke="#222" stroke-width="2"><path d="M3 2 L11 11 L3 20"/></svg></div>
</section>

<footer class="site-footer">
  <div class="footer-brand"><span class="dot"></span>PEBBLE7DOCK</div>
  <div class="footer-copy">
    <p>Quod eam tuetur, ut de vite potissimum loquar, est id extrinsecus; Atque hoc loco similitudines eas, quibus illi uti solent, dissimillimas proferebas. Vide, quaeso, rectumne sit. Quem si tenueris, non modo meum Ciceronem, sed etiam me ipsum abducas licebit. Nos commodius agimus.</p>
    <p>Est autem a te semper dictum nec gaudere quemquam nisi propter corpus nec dolere. Sed plane dicit quod intellegit. solent, dissimillimas proferebas. Vide, quaeso, rectumne sit. Quem si tenueris, non modo meum</p>
  </div>
  <div class="contact">
    <h3>Get in Touch</h3>
    <strong>Pebble7dock</strong><br>
    48 Linden Row<br>
    Harlow Bay, NY, 10999<br>
    555-201-3390
    <div class="socials"><span></span><span></span><span></span></div>
  </div>
  <div class="to-top"><svg width="16" height="10" viewBox="0 0 16 10" fill="none" stroke="#fff" stroke-width="2.2"><path d="M2 8 L8 2 L14 8"/></svg></div>
</footer>

</body>
</html>
```